Family Conference for a Church needs a creative & colorful flyer

We need a flyer that depicts the following information to be uploaded to our church website and church friendloop in order to draw maximum attention. The image should be jpg format so that it can be easily uploaded.
Information to be added in the flyer: Please be creative !!!
1. The Second Annual
2. VELMARA SINTU ( this is our brand name of the conference so please be creative in exhibiting this out )
3. Parish Family Conference
4. Growing together in Christ
5. One Church One Family One Vision
6. Presiding Spiritual Father : His Grace Dr. Lucian Tel Obrey
7. Join us for WORSHIP, RETREAT MESSAGE, INTERACTIVE SESSIONS, WORKSHOPS
8. Save the date : Saturday November 2, 2013
9. CONTACT: Rev. Fr. K.R. Donal RTPAE 2871 Castowick Lane, Bensalem PA 19388
I have uploaded a flyer called LARK for your guide only. Use that as your reference, for example LARK is VELMARA SINTU for our flyer. I want my flyer to be better than that.
Second upload is a picture which I would like to be added to the flyer as a watermark effect but at the same time visible like a black & white picture or what ever is the best that you feel.
The flyer should be printable and be easily uploaded to friendloop. ( jpg image )
Church people of all ages
Church

```html
<!DOCTYPE html>
<html lang="en">
<head>
<meta charset="utf-8">
<title>Velmara Sintu – Parish Family Conference</title>
<link rel="stylesheet" href="https://fonts.googleapis.com/css2?family=Oswald:wght@400;500;600;700&display=swap">
<style>
  :root {
    --brown-deep: #3a3028;
    --brown-mid: #5a4c40;
    --gold: #f7c500;
    --gold-light: #ffe14a;
    --gold-dark: #e8a800;
    --white: #ffffff;
  }
  html, body { margin: 0; padding: 0; overflow: hidden; background: #222; }
  .flyer {
    position: relative;
    width: 800px; height: 1200px; overflow: hidden;
    background: radial-gradient(ellipse at 50% 55%, var(--brown-mid) 0%, var(--brown-deep) 75%);
    font-family: 'Oswald', sans-serif;
    color: var(--white);
    text-align: center;
  }
  .hero-photo {
    position: absolute; left: 0; top: 0; width: 800px; height: 410px;
    background:
      linear-gradient(180deg, rgba(255,255,255,0.0) 60%, rgba(60,40,30,0.45) 100%),
      radial-gradient(ellipse at 50% 30%, #c4202a 0%, #a5252b 22%, #e9e1db 45%, #9c8f86 70%, #4a3a33 100%);
  }
  .hero-curve { position: absolute; left: 0; top: 320px; width: 800px; height: 120px; }
  .frame {
    position: absolute; left: 24px; top: 24px; width: 752px; height: 1152px;
    box-sizing: border-box; border: 2px solid var(--gold);
  }
  .block { position: absolute; left: 0; width: 800px; }
  .kicker {
    top: 400px; font-size: 34px; font-weight: 600; letter-spacing: 1px;
    display: flex; justify-content: center; align-items: center; gap: 14px;
  }
  .bars { display: inline-block; width: 80px; height: 10px;
    border-top: 3px solid var(--gold); border-bottom: 3px solid var(--gold); box-sizing: border-box; }
  .bars.short { width: 30px; }
  .brand {
    font-weight: 700; color: var(--gold); line-height: 1; font-size: 155px;
    background: linear-gradient(180deg, var(--gold-light) 0%, var(--gold) 55%, var(--gold-dark) 100%);
    -webkit-background-clip: text; background-clip: text; -webkit-text-fill-color: transparent;
    letter-spacing: 1px;
  }
  .brand-top { top: 440px; }
  .brand-bottom { top: 588px; }
  .subtitle { top: 754px; font-size: 32px; font-weight: 500;
    display: flex; justify-content: center; align-items: center; gap: 10px; }
  .date { top: 812px; font-size: 48px; font-weight: 600; }
  .date .accent { color: var(--gold); }
  .rule { position: absolute; left: 96px; width: 608px; height: 2px; background: var(--gold); opacity: 0.85; }
  .rule-top { top: 896px; }
  .rule-bottom { top: 997px; }
  .theme { top: 904px; font-size: 32px; font-weight: 600; line-height: 38px; }
  .details { top: 1040px; font-size: 17px; font-weight: 400; line-height: 22px; }
  .details strong { font-weight: 700; }
  .contact { top: 1114px; font-size: 18px; font-weight: 400; letter-spacing: 0.5px; }
</style>
</head>
<body>
<div class="flyer">
  <div class="hero-photo" role="img" aria-label="Photograph of a congregation standing in a church nave facing a red sanctuary with the altar"></div>
  <svg class="hero-curve" viewBox="0 0 800 120" preserveAspectRatio="none" aria-hidden="true">
    <path d="M0 80 Q400 -30 800 80 L800 120 L0 120 Z" fill="#3f342b"/>
    <path d="M0 80 Q400 -30 800 80" fill="none" stroke="#ffffff" stroke-width="8"/>
    <path d="M0 90 Q400 -20 800 90" fill="none" stroke="#f7c500" stroke-width="5"/>
  </svg>
  <div class="frame"></div>

  <div class="block kicker"><span class="bars"></span>THE SECOND ANNUAL<span class="bars"></span></div>
  <div class="block brand brand-top">VELMARA</div>
  <div class="block brand brand-bottom">SINTU</div>
  <div class="block subtitle"><span class="bars short"></span>PARISH FAMILY CONFERENCE<span class="bars short"></span></div>
  <div class="block date">SATURDAY <span class="accent">NOVEMBER 2, 2013</span></div>

  <div class="rule rule-top"></div>
  <div class="block theme">GROWING TOGETHER IN CHRIST<br>ONE CHURCH ONE FAMILY ONE VISION</div>
  <div class="rule rule-bottom"></div>

  <div class="block details"><strong>PRESIDING SPIRITUAL FATHER :</strong> HIS GRACE DR. LUCIAN TEL OBREY<br>JOIN US FOR WORSHIP, RETREAT MESSAGE, INTERACTIVE SESSIONS, WORKSHOPS</div>
  <div class="block contact">REV. FR. K.R. DONAL RTPAE 2871 CASTOWICK LANE, BENSALEM PA 19388</div>
</div>
</body>
</html>
```